Interior Decorating and Event Styling Business Card Design

We need a business card design for a bespoke interior decorating and event styling business, mostly weddings. We also do custom paint finishes and painted floor finishes. We want something simple, organic and stylish with good colour tones used.

On our card we would like our services listed like so -

Interior Decorating
Wedding and Event Styling
Bespoke furniture paint finishes
Painted floor finishes

Industry/Entity Type

Paint

Contact Information for Business Card

Mara & Wren Design
Rosalind 0438175264
Tessa 0429357718
rosalind.partow@mailbay.com.au
tessaorkin@mwk7.com.au

```html
<!DOCTYPE html>
<html lang="en">
<head>
<meta charset="utf-8">
<title>Mara &amp; Wren Design – Business Card</title>
<link rel="stylesheet" href="https://fonts.googleapis.com/css2?family=Lato:wght@300;400;700&display=swap">
<style>
  :root {
    --page-bg: #3d3e3a;
    --sage: #5e8a66;
    --sage-dark: #4e7656;
    --sage-light: #8fb295;
    --pattern-a: #c9dccb;
    --pattern-b: #a9c7ad;
    --paper: #ffffff;
    --ink: #2f2f2f;
    --accent: #5f8f68;
    --rule: #ffffff;
  }
  * { box-sizing: border-box; margin: 0; padding: 0; }
  html, body { width: 1200px; height: 1000px; overflow: hidden; }
  body {
    background: var(--page-bg);
    font-family: "Lato", sans-serif;
    position: relative;
  }
  .card {
    position: absolute;
    left: 250px;
    width: 700px;
    height: 400px;
    background: var(--paper);
    overflow: hidden;
    box-shadow: 0 14px 30px rgba(0,0,0,0.45);
  }
  .card--front { top: 60px; }
  .card--back { top: 530px; }

  .pattern {
    position: absolute;
    left: 0; width: 100%;
    background: linear-gradient(135deg, var(--pattern-a), var(--pattern-b) 50%, var(--pattern-a));
  }
  .band {
    position: absolute;
    left: 0; width: 100%;
    background: linear-gradient(180deg, var(--sage-light) 0%, var(--sage) 45%, var(--sage-dark) 100%);
    border-top: 4px solid var(--rule);
    border-bottom: 4px solid var(--rule);
    color: var(--paper);
    text-align: center;
  }
  .brand-name {
    font-weight: 300;
    font-size: 52px;
    letter-spacing: 3px;
    color: var(--paper);
    line-height: 1;
  }
  .services {
    margin-top: 14px;
    font-weight: 400;
    font-size: 17px;
    line-height: 1.35;
    color: #eef5ef;
  }

  /* front */
  .card--front .pattern--top { top: 0; height: 118px; }
  .card--front .band { top: 118px; height: 170px; padding-top: 30px; }
  .card--front .pattern--bottom { top: 288px; height: 112px; }

  /* back */
  .card--back .pattern--top { top: 0; height: 26px; }
  .card--back .band { top: 26px; height: 168px; padding-top: 24px; }
  .card--back .brand-name { font-size: 46px; }
  .card--back .services { margin-top: 10px; font-size: 16px; line-height: 1.3; }
  .card--back .pattern--bottom { top: 378px; height: 22px; }

  .contact {
    position: absolute;
    top: 194px; left: 0; width: 100%; height: 184px;
    padding: 22px 36px 0;
    color: var(--ink);
  }
  .owners {
    font-weight: 700;
    font-size: 28px;
    color: var(--accent);
  }
  .role { font-size: 18px; margin-top: 2px; }
  .divider {
    border: 0;
    border-top: 1px solid var(--accent);
    width: 300px;
    margin: 14px 0 12px;
  }
  .phone-list { list-style: none; }
  .phone-list li {
    display: flex; align-items: center; gap: 8px;
    font-size: 19px; margin-bottom: 6px;
  }
  .phone-list .who { color: var(--accent); }
  .icon { width: 18px; height: 18px; flex: none; }
  .email-list {
    position: absolute;
    top: 26px; right: 36px;
    list-style: none;
    text-align: right;
  }
  .email-list li {
    display: flex; justify-content: flex-end; align-items: center; gap: 8px;
    font-size: 17px; margin-bottom: 8px;
  }
</style>
</head>
<body>

<section class="card card--front" aria-label="Business card front">
  <div class="pattern pattern--top" role="img" aria-label="Soft green damask pattern"></div>
  <div class="band">
    <div class="brand-name">Mara &amp; Wren Design</div>
    <p class="services">Interior Decorating | Wedding and Event Styling | Bespoke furniture paint finishes<br>Painted floor finishes</p>
  </div>
  <div class="pattern pattern--bottom" role="img" aria-label="Soft green damask pattern"></div>
</section>

<section class="card card--back" aria-label="Business card back">
  <div class="pattern pattern--top" role="img" aria-label="Soft green damask pattern"></div>
  <div class="band">
    <div class="brand-name">Mara &amp; Wren Design</div>
    <p class="services">Interior Decorating | Wedding and Event Styling<br>Bespoke furniture paint finishes<br>Painted floor finishes</p>
  </div>

  <div class="contact">
    <div class="owners">Rosalind &amp; Tessa</div>
    <div class="role">Founder&amp; Owner</div>
    <hr class="divider">
    <ul class="phone-list">
      <li>
        <svg class="icon" viewBox="0 0 24 24" aria-hidden="true"><path d="M6.6 10.8a15 15 0 0 0 6.6 6.6l2.2-2.2c.3-.3.7-.4 1-.2 1.1.4 2.3.6 3.6.6.6 0 1 .4 1 1V20c0 .6-.4 1-1 1A17 17 0 0 1 3 4c0-.6.4-1 1-1h3.5c.6 0 1 .4 1 1 0 1.3.2 2.5.6 3.6.1.3 0 .7-.2 1z" fill="#2f2f2f"/></svg>
        <span>: 0438175264 <span class="who">(Rosalind)</span></span>
      </li>
      <li>
        <svg class="icon" viewBox="0 0 24 24" aria-hidden="true"><path d="M6.6 10.8a15 15 0 0 0 6.6 6.6l2.2-2.2c.3-.3.7-.4 1-.2 1.1.4 2.3.6 3.6.6.6 0 1 .4 1 1V20c0 .6-.4 1-1 1A17 17 0 0 1 3 4c0-.6.4-1 1-1h3.5c.6 0 1 .4 1 1 0 1.3.2 2.5.6 3.6.1.3 0 .7-.2 1z" fill="#2f2f2f"/></svg>
        <span>: 0429357718 <span class="who">(Tessa)</span></span>
      </li>
    </ul>
    <ul class="email-list">
      <li>
        <span>rosalind.partow@mailbay.com.au :</span>
        <svg class="icon" viewBox="0 0 24 18" aria-hidden="true"><rect x="1" y="1" width="22" height="16" fill="none" stroke="#5f8f68" stroke-width="2"/><path d="M1 1l11 9 11-9" fill="none" stroke="#5f8f68" stroke-width="2"/></svg>
      </li>
      <li>
        <span>tessaorkin@mwk7.com.au :</span>
        <svg class="icon" viewBox="0 0 24 18" aria-hidden="true"><rect x="1" y="1" width="22" height="16" fill="none" stroke="#5f8f68" stroke-width="2"/><path d="M1 1l11 9 11-9" fill="none" stroke="#5f8f68" stroke-width="2"/></svg>
      </li>
    </ul>
  </div>

  <div class="pattern pattern--bottom" role="img" aria-label="Soft green damask pattern"></div>
</section>

</body>
</html>
```